Construction company- stationary project
business card, letterhead, envelopes, presentation folder
Construction company- stationary project -
Creative Brief
Professional
Brent Halloway
38 Percival Ln. Millbrook, NY 12545
brent.halloway@ridgefold-builders.com
www.ridgefold-builders.com
Residential contractor focused on design build, custom, and restoration projects. Emphasizing team concept
open to ideas possibly the logo

```html
<!DOCTYPE html>
<html lang="en">
<head>
<meta charset="utf-8">
<title>Ridgefold Builders Stationery</title>
<link rel="stylesheet" href="https://fonts.googleapis.com/css2?family=Cinzel:wght@400;600&display=swap">
<style>
  :root {
    --brown-dark: #3e1a18;
    --brown: #5a2622;
    --copper: #c9743c;
    --copper-light: #e89a5c;
    --ink: #5a2a24;
    --paper: #ffffff;
    --edge: #c9c2bd;
    --cream: #f5e4d4;
  }
  * { margin: 0; padding: 0; box-sizing: border-box; }
  html, body { width: 1200px; height: 756px; overflow: hidden; background: #ffffff; }
  body { position: relative; font-family: "Cinzel", serif; color: var(--ink); }

  .sheet { position: absolute; background: var(--paper); box-shadow: 0 1px 3px rgba(0,0,0,.25); border: 1px solid var(--edge); overflow: hidden; }

  .band {
    position: absolute; left: 0; right: 0;
    background: linear-gradient(90deg, var(--brown-dark) 0%, var(--brown) 30%, var(--copper) 55%, var(--brown) 75%, var(--brown-dark) 100%);
  }

  .brand { display: flex; align-items: center; gap: 8px; color: var(--brown); font-family: "Cinzel", serif; font-weight: 600; letter-spacing: .04em; white-space: nowrap; }
  .brand-mark { display: inline-block; flex: none; background: var(--brown); }
  .brand-light { color: var(--cream); }
  .brand-light .brand-mark { background: var(--cream); }

  /* Letterhead */
  .letterhead { left: 19px; top: 29px; width: 528px; height: 691px; }
  .letterhead .band-top { top: 0; height: 6px; }
  .letterhead .band-bottom { bottom: 0; height: 6px; }
  .letterhead .brand { position: absolute; left: 22px; top: 48px; font-size: 19px; }
  .letterhead .brand-mark { width: 16px; height: 16px; }
  .letterhead .footer-text { position: absolute; left: 22px; bottom: 22px; font-size: 9.5px; line-height: 1.5; letter-spacing: .03em; }

  /* Business card front */
  .card-front { left: 576px; top: 31px; width: 223px; height: 142px; }
  .card-front .band-top { top: 0; height: 4px; }
  .card-front .band-bottom { bottom: 0; height: 4px; }
  .card-front .brand { position: absolute; left: 12px; top: 16px; font-size: 9px; gap: 5px; }
  .card-front .brand-mark { width: 8px; height: 8px; }
  .card-front .holder { position: absolute; left: 104px; top: 38px; font-size: 10px; letter-spacing: .03em; }
  .card-front .details { position: absolute; left: 12px; top: 66px; font-size: 5.6px; line-height: 1.55; letter-spacing: .02em; }

  /* Business card back */
  .card-back {
    left: 811px; top: 199px; width: 228px; height: 130px; border: none;
    background: radial-gradient(ellipse at center, var(--copper) 0%, var(--brown) 45%, var(--brown-dark) 100%);
    display: flex; align-items: center; justify-content: center;
  }
  .card-back .brand { font-size: 14px; }
  .card-back .brand-mark { width: 11px; height: 11px; }

  /* Envelope */
  .envelope { left: 571px; top: 367px; width: 605px; height: 358px; }
  .envelope .flap { position: absolute; left: 0; top: 0; width: 100%; height: 96px; }
  .envelope .flap .brand { position: absolute; left: 50%; top: 50%; transform: translate(-50%, -50%); font-size: 16px; }
  .envelope .flap .brand-mark { width: 12px; height: 12px; }
  .envelope .return { position: absolute; left: 14px; top: 120px; }
  .envelope .return .brand { font-size: 17px; }
  .envelope .return .brand-mark { width: 14px; height: 14px; }
  .envelope .return-address { margin-top: 14px; font-size: 9.5px; line-height: 1.45; letter-spacing: .03em; }
</style>
</head>
<body>

  <section class="sheet letterhead" aria-label="Letterhead">
    <div class="band band-top"></div>
    <div class="brand"><span class="brand-mark"></span>Ridgefold Builders</div>
    <p class="footer-text">38 Percival Ln. Ashgrove, VT 05391<br>Cell: 607-555-0142 | www.ridgefold-builders.com</p>
    <div class="band band-bottom"></div>
  </section>

  <section class="sheet card-front" aria-label="Business card front">
    <div class="band band-top"></div>
    <div class="brand"><span class="brand-mark"></span>Ridgefold Builders</div>
    <p class="holder">Brent Halloway</p>
    <p class="details">38 Percival Ln.<br>Ashgrove, VT 05391<br>Cell: 607-555-0142<br>Email: brent.halloway@ridgefold-builders.com<br>Website: www.ridgefold-builders.com</p>
    <div class="band band-bottom"></div>
  </section>

  <section class="sheet card-back" aria-label="Business card back">
    <div class="brand brand-light"><span class="brand-mark"></span>Ridgefold Builders</div>
  </section>

  <section class="sheet envelope" aria-label="Envelope">
    <svg class="flap" viewBox="0 0 605 96" preserveAspectRatio="none" aria-hidden="true">
      <defs>
        <linearGradient id="flapFill" x1="0" x2="1" y1="0" y2="0">
          <stop offset="0" stop-color="#3e1a18"/>
          <stop offset="0.3" stop-color="#5a2622"/>
          <stop offset="0.55" stop-color="#c9743c"/>
          <stop offset="0.78" stop-color="#5a2622"/>
          <stop offset="1" stop-color="#3e1a18"/>
        </linearGradient>
      </defs>
      <path d="M0 0 H565 Q605 0 605 40 V96 H0 Z" fill="url(#flapFill)"/>
      <path d="M565 2 Q600 4 602 40" fill="none" stroke="#e89a5c" stroke-opacity=".5" stroke-width="1"/>
    </svg>
    <div class="flap"><div class="brand brand-light"><span class="brand-mark"></span>Ridgefold Builders</div></div>
    <div class="return">
      <div class="brand"><span class="brand-mark"></span>Ridgefold Builders</div>
      <p class="return-address">38 Percival Ln.<br>Ashgrove, VT 05391</p>
    </div>
  </section>

</body>
</html>
```